Bright Fern Custom Homes business card. Double sided. Modern. professional

Bright Fern Custom Homes
contemporary modern design with our logo /
Double sided with all our contact information
Use same Green colors as in our Logo. Contemporary logo that grabs your attention. Visually pleasing and balanced. Easy to read, and Vibrant. Would love an option for rounded edges. Embossed logo would be amazing.
Contact Information for Business Card
Dana Welk Owner / General Contractor Bright Fern Custom Homes p: 704.552.1830 m: 912.648.2071 e: brightferncustomhomes@mailbox.example w: www.brightferncustomhomes.example 218 Pryor Meadow Lane Crestmoor, XX 00000

```html
<!DOCTYPE html>
<html lang="en">
<head>
<meta charset="utf-8">
<title>Bright Fern Custom Homes – Business Card</title>
<link rel="stylesheet" href="https://fonts.googleapis.com/css2?family=Arimo:wght@400;700&display=swap">
<style>
  :root {
    --leaf: #739035;
    --leaf-dark: #56722b;
    --ink: #1b1c1e;
    --text: #333333;
    --paper: #ffffff;
    --backdrop: #2b2b2d;
    --rule: #555555;
  }
  * { box-sizing: border-box; margin: 0; padding: 0; }
  html, body { width: 1200px; height: 1107px; overflow: hidden; }
  body {
    background: var(--backdrop);
    font-family: "Arimo", Arial, sans-serif;
    display: flex;
    justify-content: center;
    align-items: center;
    gap: 70px;
  }
  .card {
    width: 420px;
    height: 700px;
    border-radius: 28px;
    overflow: hidden;
    position: relative;
    box-shadow: 0 18px 40px rgba(0,0,0,.45);
  }

  /* Front */
  .card--front {
    background: var(--paper);
    display: flex;
    flex-direction: column;
    align-items: center;
    padding: 90px 40px 0;
    text-align: center;
    color: var(--text);
  }
  .brand {
    display: flex;
    flex-direction: column;
    align-items: center;
    gap: 16px;
  }
  .brand__mark {
    width: 64px; height: 64px;
    background: var(--leaf);
    border-radius: 50%;
  }
  .brand__name {
    color: var(--leaf);
    font-weight: 700;
    font-size: 26px;
    line-height: 1.2;
    letter-spacing: .04em;
    text-transform: uppercase;
  }
  .person { margin-top: 64px; }
  .person__name {
    color: var(--leaf);
    font-weight: 700;
    font-size: 26px;
    letter-spacing: .02em;
  }
  .person__title { font-size: 19px; margin-top: 4px; }

  .icon-row {
    margin-top: 18px;
    width: 100%;
    display: flex;
    align-items: center;
    gap: 10px;
  }
  .icon-row__rule { flex: 1; height: 1px; background: var(--rule); }
  .icon {
    width: 34px; height: 34px;
    background: var(--leaf);
    border-radius: 6px;
    display: flex; align-items: center; justify-content: center;
  }
  .icon svg { width: 22px; height: 22px; fill: none; stroke: #fff; stroke-width: 2; stroke-linecap: round; stroke-linejoin: round; }

  .contact {
    margin-top: 14px;
    font-size: 17px;
    line-height: 1.35;
    list-style: none;
  }
  .contact__rule { width: 100%; height: 1px; background: var(--rule); margin: 20px 0 18px; }
  .address { font-size: 18px; line-height: 1.35; font-style: normal; }

  /* Back */
  .card--back { background: var(--ink); }
  .card__band {
    position: absolute; left: 0; top: 0;
    width: 100%; height: 58%;
    background: var(--leaf);
  }
  .card__band-mark {
    position: absolute;
    left: 50%; top: 150px;
    transform: translateX(-50%);
    width: 200px; height: 200px;
    border-radius: 50%;
    background: var(--leaf-dark);
    border: 10px solid var(--paper);
  }
  .card__wordmark {
    position: absolute;
    left: 0; right: 0; bottom: 110px;
    text-align: center;
    color: var(--leaf);
    font-weight: 700;
    font-size: 30px;
    line-height: 1.25;
    letter-spacing: .05em;
    text-transform: uppercase;
  }
</style>
</head>
<body>

  <section class="card card--front" aria-label="Card front">
    <div class="brand">
      <span class="brand__mark" aria-hidden="true"></span>
      <p class="brand__name">Bright Fern<br>Custom Homes</p>
    </div>

    <div class="person">
      <h1 class="person__name">DANA WELK</h1>
      <p class="person__title">Owner / General Contractor</p>
    </div>

    <div class="icon-row">
      <span class="icon-row__rule"></span>
      <span class="icon" aria-label="Phone">
        <svg viewBox="0 0 24 24"><path d="M5 4h4l2 5-2.5 1.5a11 11 0 0 0 5 5L15 13l5 2v4a2 2 0 0 1-2 2A16 16 0 0 1 3 6a2 2 0 0 1 2-2"/></svg>
      </span>
      <span class="icon" aria-label="Mobile">
        <svg viewBox="0 0 24 24"><rect x="7" y="3" width="10" height="18" rx="2"/><path d="M11 18h2"/></svg>
      </span>
      <span class="icon" aria-label="Email">
        <svg viewBox="0 0 24 24"><rect x="3" y="6" width="18" height="12" rx="1"/><path d="M3 6l9 7 9-7"/></svg>
      </span>
      <span class="icon" aria-label="Website">
        <svg viewBox="0 0 24 24"><circle cx="12" cy="12" r="9"/><path d="M3 12h18M12 3a14 14 0 0 1 0 18M12 3a14 14 0 0 0 0 18"/></svg>
      </span>
      <span class="icon-row__rule"></span>
    </div>

    <ul class="contact">
      <li>704.552.1830</li>
      <li>912.648.2071</li>
      <li>brightferncustomhomes@mailbox.example</li>
      <li>www.brightferncustomhomes.example</li>
    </ul>

    <div class="contact__rule"></div>

    <address class="address">218 Pryor Meadow Lane<br>Crestmoor, XX 00000</address>
  </section>

  <section class="card card--back" aria-label="Card back">
    <div class="card__band"></div>
    <span class="card__band-mark" aria-hidden="true"></span>
    <p class="card__wordmark">Bright Fern<br>Custom Homes</p>
  </section>

</body>
</html>
```